KORBALT

The business want a professional looking business card. We have a scetch we will add but want the extra upgrade, and would like more suggestions for variations of our business cards.

```html
<!DOCTYPE html>
<html lang="en">
<head>
<meta charset="utf-8">
<title>KORBALT business card</title>
<link rel="stylesheet" href="https://fonts.googleapis.com/css2?family=Playfair+Display:wght@600;700&family=Poppins:wght@400;500&display=swap">
<style>
  :root {
    --page: #806232;
    --gold-light: #e0d3b1;
    --gold-mid: #ccb373;
    --gold-deep: #a4874c;
    --gold-dark: #80602f;
    --ink: #7b5a2c;
    --shade: rgba(120, 88, 40, 0.16);
    --band: rgba(150, 120, 70, 0.35);
    --mark: #d3bd7c;
  }
  * { margin: 0; padding: 0; box-sizing: border-box; }
  html, body { width: 1200px; height: 1200px; overflow: hidden; }
  body { background: var(--page); position: relative; font-family: "Poppins", sans-serif; }
  .card {
    position: absolute; left: 285px; width: 630px; height: 406px; overflow: hidden;
    background: linear-gradient(90deg, var(--gold-light) 0%, var(--gold-mid) 46%, #c6ad6c 52%, var(--gold-deep) 72%, var(--gold-dark) 100%);
  }
  .card-front { top: 147px; }
  .card-back { top: 620px; }
  .card-shapes { position: absolute; inset: 0; width: 100%; height: 100%; }
  .company-name {
    position: absolute; left: 19px; top: 66px;
    font-family: "Playfair Display", serif; font-weight: 700; font-size: 36px;
    color: var(--ink); letter-spacing: 0.5px; white-space: nowrap;
  }
  .role { position: absolute; left: 21px; top: 110px; font-size: 12px; letter-spacing: 3px; color: var(--ink); }
  .person { position: absolute; left: 20px; top: 127px; font-size: 17px; font-weight: 500; letter-spacing: 2px; color: var(--ink); }
  .contact-list { position: absolute; left: 28px; top: 210px; list-style: none; }
  .contact-list li { display: flex; align-items: center; height: 37.5px; font-size: 19px; color: var(--ink); }
  .contact-list svg { width: 26px; height: 26px; margin-right: 11px; flex: none; }
  .corner-name {
    position: absolute; left: 450px; top: 86px; width: 124px; text-align: center;
    font-family: "Playfair Display", serif; font-weight: 700; font-size: 26px; color: var(--mark);
  }
  .brand-name {
    position: absolute; left: 0; right: 0; top: 168px; text-align: center;
    font-family: "Playfair Display", serif; font-weight: 700; font-size: 64px; color: var(--ink); letter-spacing: 1px;
  }
  .brand-since {
    position: absolute; left: 0; right: 0; top: 248px; text-align: center;
    font-family: "Playfair Display", serif; font-weight: 600; font-size: 16px; color: var(--ink); letter-spacing: 12px; padding-left: 12px;
  }
</style>
</head>
<body>
  <section class="card card-front">
    <svg class="card-shapes" viewBox="0 0 1010 652" preserveAspectRatio="none" aria-hidden="true">
      <rect x="0" y="73" width="451" height="14" fill="var(--band)"/>
      <polygon points="0,409 243,652 0,652" fill="var(--shade)"/>
      <polygon points="776,422 546,652 1010,652" fill="var(--shade)"/>
    </svg>
    <h1 class="company-name">KORBALT BRENNVIK</h1>
    <p class="role">CEO &amp; Founder</p>
    <p class="person">Aksel Brennvik</p>
    <ul class="contact-list">
      <li>
        <svg viewBox="0 0 24 24" aria-hidden="true"><rect x="6" y="1.5" width="12" height="21" rx="2" fill="none" stroke="var(--ink)" stroke-width="2"/><circle cx="12" cy="19" r="1" fill="var(--ink)"/></svg>
        004790146273
      </li>
      <li>
        <svg viewBox="0 0 24 24" aria-hidden="true"><rect x="2" y="5" width="20" height="14" fill="none" stroke="var(--ink)" stroke-width="2"/><polyline points="2,5 12,13 22,5" fill="none" stroke="var(--ink)" stroke-width="2"/></svg>
        korbalt.llc@postmail.com
      </li>
      <li>
        <svg viewBox="0 0 24 24" aria-hidden="true"><g fill="none" stroke="var(--ink)" stroke-width="1.5"><circle cx="12" cy="12" r="10"/><ellipse cx="12" cy="12" rx="4.5" ry="10"/><line x1="2" y1="12" x2="22" y2="12"/><line x1="4" y1="7" x2="20" y2="7"/><line x1="4" y1="17" x2="20" y2="17"/></g></svg>
        www.korbalt.llc
      </li>
    </ul>
    <p class="corner-name">KORBALT</p>
  </section>

  <section class="card card-back">
    <svg class="card-shapes" viewBox="0 0 1018 658" preserveAspectRatio="none" aria-hidden="true">
      <rect x="0" y="74" width="457" height="14" fill="var(--band)"/>
      <polygon points="230,426 0,658 462,658" fill="var(--shade)"/>
      <polygon points="786,418 554,650 1018,650" fill="var(--shade)"/>
    </svg>
    <h2 class="brand-name">KORBALT</h2>
    <p class="brand-since">SINCE 2026</p>
  </section>
</body>
</html>
```